Valve bag design

I need a valve bag for 25kg wall putty bag

Here are attached bags for reference

Most of the words or design you can copy from mablunt bag attached and company profile
Also I have attached our local product for reference

```html
<!DOCTYPE html>
<html lang="en">
<head>
<meta charset="utf-8">
<title>Crest Coat Wall Putty – Bag Artwork</title>
<link href="https://fonts.googleapis.com/css2?family=Poppins:wght@400;500;600;700;800&family=Barlow+Semi+Condensed:wght@600;700&display=swap" rel="stylesheet">
<style>
  :root{
    --navy:#1f3a6e;
    --navy-deep:#14295a;
    --taupe:#b0a59e;
    --panel:#ffffff;
    --stage:#f3f3f3;
    --box:#e3e3e3;
    --ink:#222;
    --sky-light:#eef1f7;
    --sky:#c9d3e6;
  }
  *{box-sizing:border-box;margin:0;padding:0}
  html,body{width:758px;height:1200px;overflow:hidden}
  body{background:var(--stage);font-family:'Poppins',sans-serif;color:var(--ink);position:relative}
  .panel{position:absolute;top:341px;width:345px;height:518px;background:var(--panel);overflow:hidden;box-shadow:0 4px 14px rgba(0,0,0,.12)}
  .panel--front{left:24px}
  .panel--back{left:389px}
  .swoosh{position:absolute;inset:0;width:345px;height:518px}

  /* corner brand marks, shown as plain squares */
  .corner-mark{position:absolute;width:30px;height:30px;background:var(--navy)}
  .corner-mark--top{left:12px;top:12px}
  .corner-mark--bottom{right:12px;bottom:12px}

  /* front */
  .brand{position:absolute;left:0;right:0;top:74px;text-align:center}
  .brand__name{font-family:'Poppins',sans-serif;font-weight:700;font-size:21px;letter-spacing:1.5px;color:var(--navy);line-height:1}
  .title{position:absolute;left:0;right:0;top:104px;text-align:center;font-weight:800;font-size:42px;line-height:1;color:var(--navy-deep);letter-spacing:.5px}
  .subtitle{position:absolute;left:52px;width:241px;top:155px;height:21px;background:var(--taupe);color:#fff;text-align:center;font-family:'Barlow Semi Condensed',sans-serif;font-weight:700;font-size:15px;line-height:21px;letter-spacing:.3px}
  .cityscape{position:absolute;left:58px;top:184px;width:214px;height:156px;background:linear-gradient(180deg,var(--sky-light) 0%,var(--sky) 100%)}
  .claim{position:absolute;left:0;right:0;top:374px;text-align:center;font-weight:700;font-size:7.6px;line-height:10px;color:#111}
  .feature{position:absolute;width:90px;text-align:center;font-size:5.6px;line-height:6.8px;color:#333}
  .feature__icon{display:block;margin:0 auto 3px;width:23px;height:23px;border-radius:50%;background:var(--navy);position:relative}
  .feature__icon svg{position:absolute;inset:5px;width:13px;height:13px}
  .weight{position:absolute;left:18px;top:473px;color:var(--navy-deep)}
  .weight__label{font-size:4.8px;color:#333;display:block}
  .weight__value{font-weight:700;font-size:23px;line-height:1}
  .weight__unit{font-weight:700;font-size:8px}

  /* back */
  .badge{position:absolute;left:136px;top:20px;width:72px;height:72px;border-radius:50%;background:#e6e6e6;display:flex;align-items:center;justify-content:center}
  .badge .brand__name{font-size:8px;letter-spacing:.4px}
  .info{position:absolute;left:27px;top:99px;width:291px;height:359px;background:var(--box);padding:18px 12px 0}
  .info p{font-size:5.5px;line-height:6.9px;color:#333;margin-bottom:5.4px}
  .notes{position:absolute;left:12px;right:18px;top:258px;height:42px;border:1px solid var(--navy);padding:5px 6px 0 28px}
  .notes p{font-size:4.9px;line-height:6px;margin-bottom:4px}
  .notes b{color:var(--navy);font-weight:600}
  .notes__icon{position:absolute;left:7px;width:12px;height:12px}
  .weight--back{left:12px;top:306px}
  .weight--back .weight__label{font-size:5.6px}
  .weight--back .weight__value{font-size:26px}
  .specs{position:absolute;left:86px;top:306px;width:187px;border:1px solid var(--navy);border-collapse:collapse;font-size:4.6px;color:#333}
  .specs th,.specs td{border:1px solid var(--navy);padding:1.5px 6px;text-align:left;height:8.5px}
  .specs th{font-weight:600;font-size:5.4px;color:#111}
  .footer{position:absolute;left:33px;right:50px;top:474px;display:flex;justify-content:space-between;align-items:flex-end;font-size:6.5px;line-height:8.4px}
  .footer__label{color:#222}
  .footer strong{color:var(--navy);font-weight:700}
</style>
</head>
<body>

<section class="panel panel--front" aria-label="Bag front">
  <svg class="swoosh" viewBox="0 0 345 518" aria-hidden="true">
    <path d="M0 198 C28 300 120 344 232 340 C140 340 52 322 0 286 Z" fill="var(--navy)"/>
    <path d="M345 222 C322 300 262 350 118 362 C238 364 318 336 345 302 Z" fill="var(--taupe)"/>
  </svg>
  <span class="corner-mark corner-mark--top" aria-hidden="true"></span>
  <span class="corner-mark corner-mark--bottom" aria-hidden="true"></span>
  <div class="brand"><span class="brand__name">CREST COAT</span></div>
  <h1 class="title">WALL PUTTY</h1>
  <div class="subtitle">WHITE CEMENT BASED PUTTY</div>
  <div class="cityscape" role="img" aria-label="Pencil sketch of a city skyline with tall towers"></div>
  <p class="claim">PREMIUM WALL PUTTY TO USE FOR CEMENT BOVED PLASTER<br>$ CONCRETE SURFACES BEFORE POINT</p>

  <div class="feature" style="left:17px;top:396px"><span class="feature__icon"><svg viewBox="0 0 13 13"><path d="M9 2a5 5 0 1 0 2 7 4 4 0 0 1-2-7z" fill="#fff"/></svg></span>Very smooth<br>and glossy finish</div>
  <div class="feature" style="left:95px;top:396px"><span class="feature__icon"><svg viewBox="0 0 13 13"><path d="M2 11V5l4.5-3L11 5v6z" fill="#fff"/></svg></span>Suitable for all<br>cement surfaces</div>
  <div class="feature" style="left:176px;top:396px"><span class="feature__icon"><svg viewBox="0 0 13 13"><rect x="2" y="2" width="9" height="9" fill="none" stroke="#fff" stroke-width="1.4"/><path d="M2 6.5h9M6.5 2v9" stroke="#fff" stroke-width="1"/></svg></span>Suitable for Interior<br>of exterior</div>
  <div class="feature" style="left:246px;top:406px"><span class="feature__icon"><svg viewBox="0 0 13 13"><path d="M3 10l6-7 2 2-7 6z" fill="#fff"/></svg></span>Very high tenate<br>adhesion</div>
  <div class="feature" style="left:45px;top:438px"><span class="feature__icon"><svg viewBox="0 0 13 13"><path d="M6.5 1L10 7a3.5 3.5 0 0 1-7 0z" fill="#fff"/></svg></span>Very low water<br>absorption</div>
  <div class="feature" style="left:125px;top:438px"><span class="feature__icon"><svg viewBox="0 0 13 13"><circle cx="6.5" cy="6.5" r="5" fill="none" stroke="#fff" stroke-width="1.4"/><path d="M3 3l7 7" stroke="#fff" stroke-width="1.4"/></svg></span>No water caring,<br>needed</div>
  <div class="feature" style="left:203px;top:438px"><span class="feature__icon"><svg viewBox="0 0 13 13"><path d="M1 7a5.5 5.5 0 0 1 11 0z" fill="#fff"/><path d="M6.5 7v4" stroke="#fff" stroke-width="1.2"/></svg></span>Very high coverage<br>&amp; easy to apply</div>

  <div class="weight"><span class="weight__label">NET WEIGHT</span><span class="weight__value">25</span> <span class="weight__unit">kg</span></div>
</section>

<section class="panel panel--back" aria-label="Bag back">
  <svg class="swoosh" viewBox="0 0 345 518" aria-hidden="true">
    <path d="M0 212 C20 290 60 330 120 340 L120 360 C60 352 20 335 0 330 Z" fill="var(--navy)"/>
    <path d="M345 236 C330 300 300 330 250 345 L250 360 C300 356 330 348 345 342 Z" fill="var(--taupe)"/>
  </svg>
  <span class="corner-mark corner-mark--top" aria-hidden="true"></span>
  <span class="corner-mark corner-mark--bottom" aria-hidden="true"></span>
  <div class="badge"><span class="brand__name">CREST COAT</span></div>

  <div class="info">
    <p>Description: this wall putty is a white cement based filler that gives an ideal smooth base for plastered walls and ceilings. It reduces paint consumption, gives an even ground for paint and resists moisture, so later repainting needs less material. Keep bags away from humid air and physical damage, and store them off the floor.<br>Application recommendations</p>
    <p>Apply on cement concrete, cement plaster surfaces, wallboard and gypsum plaster. Add one 25 kg bag to about ten litres of clean water and mix with a slow electric mixer until smooth and free of lumps.</p>
    <p>Let the mixed putty rest for a few minutes and mix again before use.</p>
    <p>The mortar must be used in 2 - 3 hours.</p>
    <p>Remove all dust, loose particles, oil, paint, curing agent, lime and silicone from the surface before application of the wall putty.</p>
    <p>Dampen the surface before the application. Cracks and holes must be repaired with a suitable mortar first.</p>
    <p>Apply the 1st coat of wall putty (1.5 mm thickness) using a blade / spatula on the wall with a "bottom to up" direction.</p>
    <p>Apply the 2nd coat of wall putty (1.0 mm thickness) preferably after 4 hours during summers, and after 12 hours during winters. Second coat shall be applied</p>
    <p>Apply the 1st coat of wall putty (1.5 mm thickness) using a blade / spatula on the wall with a "bottom to up" direction.</p>
    <p>Apply the 2nd coat of wall putty (1.0 mm thickness) preferably after 4 hours during summers, and after 12 hours during winters. Second coat shall be applied</p>
    <p>horizontally to even out application marks of 1st coat, if any.</p>

    <div class="notes">
      <svg class="notes__icon" style="top:4px" viewBox="0 0 12 12" aria-hidden="true"><rect x="1" y="7" width="2" height="4" fill="var(--ink)"/><rect x="5" y="5" width="2" height="6" fill="var(--ink)"/><rect x="9" y="2" width="2" height="9" fill="var(--ink)"/></svg>
      <p><b>Consumption:</b> Approximately 1kg/m (for 1 mm thickness)</p>
      <svg class="notes__icon" style="top:20px" viewBox="0 0 12 12" aria-hidden="true"><circle cx="6" cy="6" r="5" fill="none" stroke="var(--ink)" stroke-width="1.2"/><path d="M6 3v3l2 2" stroke="var(--ink)" stroke-width="1.2" fill="none"/></svg>
      <p><b>Shelf life:</b> Unopened bag can be stored in dry environment for up to 12<br>months, staked</p>
    </div>

    <div class="weight weight--back"><span class="weight__label">NET WEIGHT</span><span class="weight__value">25</span> <span class="weight__unit">kg</span></div>
    <table class="specs">
      <tr><th>Product specifications</th><th></th></tr>
      <tr><td>Compressive Strenght</td><td>28 days - 14 N/mm</td></tr>
      <tr><td>Adhesion Strenght</td><td>28 days - 2.38 N/mm</td></tr>
      <tr><td>Water requirement by volume</td><td>38%</td></tr>
    </table>
  </div>

  <div class="footer">
    <div><span class="footer__label">Marteted and distributed by:</span><br><strong>Halden Build Ltd</strong><br><strong>TEL: +255700123450)</strong></div>
    <div><strong>info@haldenbuild.com</strong><br><strong>haldenbuild.com</strong></div>
  </div>
</section>

</body>
</html>
```